The Ashcombe- outdoor banner

This should be a horizontal banner. It should have the logos attached incorporated and the following details
Coming Spring 2025: The Ashcombe - Exclusive Luxury Condos
Listed by Marisol Avenell | Quillfield Realty
Construction by Pinegate Builders
Unveil the height of luxury living with The Ashcombe, a new condo building in East Boston, set for completion in Spring 2025. Experience a standard of elegance and sophistication like never before.
For more information and inquiries, please contact:
Marisol Avenell
Phone: (617) 490-7163
Email: marisol@quillfieldhomes.example
The banner should be very classy incorporting gold and navy very classic fonts. The Ashcombe should look very classy and exclusive. The pinegate builders logo should be smaller. It should not include their phone number and instagram handle only the name of the company. Herringbone pattern in the background would be great. This is going outside the building to advertise pre construction units

```html
<!DOCTYPE html>
<html lang="en">
<head>
<meta charset="utf-8">
<title>The Ashcombe – Outdoor Banner</title>
<link href="https://fonts.googleapis.com/css2?family=Crimson+Text:ital,wght@0,400;0,600;0,700;1,700&display=swap" rel="stylesheet">
<style>
  :root {
    --navy: #24324f;
    --navy-deep: #1f2b45;
    --gold: #e9b661;
    --white: #ffffff;
    --page: #ffffff;
  }
  html, body {
    margin: 0;
    padding: 0;
    width: 1200px;
    height: 1200px;
    overflow: hidden;
    background: var(--page);
  }
  .canvas {
    position: relative;
    width: 1200px;
    height: 1200px;
  }
  .banner {
    position: absolute;
    left: 50px;
    top: 416px;
    width: 1100px;
    height: 365px;
    background: var(--white);
    overflow: hidden;
    font-family: "Crimson Text", "Times New Roman", serif;
    box-shadow: 6px 6px 8px rgba(0,0,0,0.25);
  }
  .banner-waves {
    position: absolute;
    inset: 0;
    width: 1100px;
    height: 365px;
  }
  .headline-block {
    position: absolute;
    left: 65px;
    top: 38px;
    color: var(--navy);
    white-space: nowrap;
  }
  .headline {
    margin: 0;
    font-size: 35px;
    font-weight: 700;
    line-height: 40px;
  }
  .credit {
    margin: 0;
    font-size: 27px;
    font-weight: 400;
    line-height: 31px;
  }
  .description {
    position: absolute;
    left: 65px;
    top: 195px;
    width: 620px;
    margin: 0;
    color: var(--white);
    font-size: 14.5px;
    line-height: 21px;
  }
  .contact {
    position: absolute;
    left: 65px;
    top: 256px;
    color: var(--white);
    white-space: nowrap;
  }
  .contact-prompt {
    margin: 0;
    color: var(--gold);
    font-size: 19.5px;
    font-style: italic;
    font-weight: 700;
    line-height: 23px;
  }
  .contact-name {
    margin: 0;
    font-size: 18.5px;
    line-height: 23px;
  }
  .contact-details {
    margin: 0;
    font-size: 18.5px;
    font-weight: 700;
    line-height: 23px;
  }
  .brand {
    position: absolute;
    display: flex;
    align-items: center;
    justify-content: center;
    font-family: "Crimson Text", "Times New Roman", serif;
    font-weight: 600;
    text-align: center;
  }
  .brand-realty {
    left: 805px;
    top: 259px;
    width: 98px;
    height: 72px;
    background: var(--navy-deep);
    outline: 1px solid rgba(255,255,255,0.08);
    color: var(--white);
    font-size: 13px;
    line-height: 1.15;
  }
  .brand-builder {
    left: 945px;
    top: 268px;
    width: 92px;
    height: 54px;
    background: var(--white);
    color: var(--navy);
    font-size: 12px;
    line-height: 1.15;
  }
</style>
</head>
<body>
<div class="canvas">
  <section class="banner" aria-label="The Ashcombe outdoor banner">
    <svg class="banner-waves" viewBox="0 0 1100 365" aria-hidden="true">
      <path fill="var(--navy)" d="M0,161 C200,150 400,166 537,172 C800,178 1000,122 1100,24 L1100,365 L0,365 Z"/>
      <path fill="var(--gold)" d="M537,171 C790,168 990,100 1100,0 L1100,24 C1000,122 800,178 537,172 Z"/>
      <path fill="var(--navy)" d="M537,171 C650,148 800,128 905,136 C860,150 720,166 537,171 Z"/>
    </svg>

    <header class="headline-block">
      <h1 class="headline">Coming Spring 2025: The Ashcombe - Exclusive Luxury Condos</h1>
      <p class="credit">Listed by Marisol Avenell | Quillfield Realty<br>Construction by Pinegate Builders</p>
    </header>

    <p class="description">Unveil the height of luxury living with The Ashcombe, a new condo building in East Boston, set for completion in Spring 2025. Experience a standard of elegance and sophistication like never before.</p>

    <div class="contact">
      <p class="contact-prompt">For more information and inquiries, please contact:</p>
      <p class="contact-name">Marisol Avenell</p>
      <p class="contact-details">(617) 490-7163 | marisol@quillfieldhomes.example</p>
    </div>

    <div class="brand brand-realty">Quillfield<br>Realty</div>
    <div class="brand brand-builder">Pinegate<br>Builders</div>
  </section>
</div>
</body>
</html>
```